KeyHarbor needs a modern business card

We are a modern conveyancing company and we need to appeal to the top (Multi-million dollar properties)and bottom on the property conveyancing market but our sweet spot is the middle of the market. I like professional with a hint of unconventional.

Target Market(s)

As above

Industry/Entity Type

Real Estate

Contact Information for Business Card

Back Of card:
thinking black with the logo and a tag line (I could be wrong about the black)
Tag line - Clear Guidance, Dependable Service

Front of Card:
Marissa Toll (BBus (Finance) LLB)
Licensed Conveyancer
Email: marissa@keyharbor.com.au

Key Harbor
ABN: 48 913 706
Suite 14, Level 3, 9 Calloway Road Lindhurst Park, NSW 2178
Phone: 1300 682 917

Sydney - Melbourne - Brisbane (Perhaps have this along the bottom of the card)

Requirements
Must have
• Sleek, modern and top end appeal (But approachable)
Should not have
• Not too cluttered

```html
<!DOCTYPE html>
<html lang="en">
<head>
<meta charset="utf-8">
<title>KeyHarbor Business Card</title>
<link rel="stylesheet" href="https://fonts.googleapis.com/css2?family=Open+Sans:wght@400;600;700&display=swap">
<style>
  :root {
    --stage: #3a3431;
    --card: #141414;
    --card-edge: #1e1e1e;
    --ink: #f2f2f2;
    --muted: #bdbdbd;
    --blue: #2f7fc0;
    --green: #7cc242;
    --rule: #5a5a5a;
    --mark-grey: #8a8a8a;
    --name-grey: #cfcfcf;
  }
  * { box-sizing: border-box; margin: 0; padding: 0; }
  html, body {
    width: 1200px; height: 814px; overflow: hidden;
    background: var(--stage);
    font-family: "Open Sans", Arial, sans-serif;
  }
  .stage {
    position: relative; width: 1200px; height: 814px;
    display: flex; align-items: center; justify-content: center; gap: 44px;
  }
  .card {
    position: relative; width: 520px; height: 318px;
    background: var(--card);
    border: 1px solid var(--card-edge);
    border-radius: 4px;
    box-shadow: 0 12px 30px rgba(0,0,0,.45);
    color: var(--ink);
    overflow: hidden;
  }
  /* Front */
  .brand {
    position: absolute; left: 36px; top: 118px;
    display: flex; align-items: center; gap: 10px;
  }
  .brand-mark { width: 24px; height: 24px; background: var(--blue); flex: none; }
  .brand-name { font-size: 24px; font-weight: 600; color: var(--ink); letter-spacing: -.3px; white-space: nowrap; }
  .divider {
    position: absolute; left: 236px; top: 34px; width: 1px; height: 170px;
    background: linear-gradient(to bottom, transparent, var(--rule) 20%, var(--rule) 80%, transparent);
  }
  .details { position: absolute; left: 256px; top: 36px; font-size: 12.5px; line-height: 1.45; white-space: nowrap; }
  .person-name { font-size: 16px; font-weight: 600; color: var(--blue); line-height: 1.3; }
  .person-quals { color: var(--blue); }
  .person-role { color: var(--green); margin-bottom: 4px; }
  .address, .abn { color: var(--ink); }
  .abn { margin-bottom: 6px; }
  .contact-line { display: flex; align-items: center; gap: 8px; color: var(--ink); }
  .contact-line svg { width: 12px; height: 12px; fill: var(--blue); flex: none; }
  .cities {
    position: absolute; left: 0; right: 0; bottom: 34px; text-align: center;
    font-size: 14px; font-weight: 700; color: var(--ink); padding-left: 60px;
  }
  /* Back */
  .back-brand {
    position: absolute; left: 0; right: 0; top: 96px;
    display: flex; align-items: center; justify-content: center; gap: 14px;
  }
  .back-brand .brand-mark { width: 30px; height: 30px; background: var(--mark-grey); }
  .back-brand .brand-name { font-size: 32px; color: var(--name-grey); }
  .tagline {
    position: absolute; left: 0; right: 0; top: 200px; text-align: center;
    font-size: 12px; color: var(--muted); padding-left: 90px;
  }
</style>
</head>
<body>
<main class="stage">
  <section class="card card-front" aria-label="Front of business card">
    <div class="brand">
      <span class="brand-mark"></span>
      <span class="brand-name">KeyHarbor</span>
    </div>
    <div class="divider"></div>
    <div class="details">
      <p class="person-name">Marissa Toll</p>
      <p class="person-quals">(BBus (Finance) LLB)</p>
      <p class="person-role">Licensed Conveyancer</p>
      <p class="address">Suite 14, Level 3, 9 Calloway Road<br>Lindhurst Park, NSW 2178</p>
      <p class="abn">ABN: 48 913 706</p>
      <p class="contact-line">
        <svg viewBox="0 0 24 24" aria-hidden="true"><path d="M6.6 10.8a15.1 15.1 0 0 0 6.6 6.6l2.2-2.2c.3-.3.7-.4 1-.2 1.1.4 2.3.6 3.6.6.6 0 1 .4 1 1V20c0 .6-.4 1-1 1A17 17 0 0 1 3 4c0-.6.4-1 1-1h3.5c.6 0 1 .4 1 1 0 1.3.2 2.5.6 3.6.1.3 0 .7-.2 1z"/></svg>
        <span>1300 682 917</span>
      </p>
      <p class="contact-line">
        <svg viewBox="0 0 24 24" aria-hidden="true"><path d="M2 5h20v14H2z M2 5l10 8 10-8" stroke="#141414" stroke-width="1.6"/></svg>
        <span>marissa@keyharbor.com.au</span>
      </p>
    </div>
    <p class="cities">Sydney - Melbourne - Brisbane</p>
  </section>

  <section class="card card-back" aria-label="Back of business card">
    <div class="back-brand">
      <span class="brand-mark"></span>
      <span class="brand-name">KeyHarbor</span>
    </div>
    <p class="tagline">Clear Guidance, Dependable Service</p>
  </section>
</main>
</body>
</html>
```